Corvale Real Estate

I manage 2 firms. The first one is Felmont and the logo is in blue (see the file) but i need a design for my business card for the second firm called CORVALE IMMOBILIER. This one is in charge of Real estate developer.

Colors
3176b5

```html
<!DOCTYPE html>
<html lang="fr">
<head>
<meta charset="utf-8">
<title>Corvale Immobilier – Business cards</title>
<link rel="stylesheet" href="https://fonts.googleapis.com/css2?family=Montserrat:wght@400;600;700&family=Libre+Baskerville&display=swap">
<style>
  :root {
    --brand-blue: #3b59a8;
    --brand-grey: #9b9b9b;
    --card-white: #ffffff;
    --stage-dark: #3a3735;
    --page-white: #ffffff;
    --label-light: #e4e2df;
  }
  * { box-sizing: border-box; margin: 0; padding: 0; }
  html, body { width: 902px; height: 1200px; overflow: hidden; }
  body {
    position: relative;
    background: var(--page-white);
    font-family: "Montserrat", Arial, sans-serif;
  }
  .stage {
    position: absolute; left: 0; top: 0; width: 902px; height: 773px;
    background: var(--stage-dark);
  }
  .card {
    position: absolute;
    background: var(--card-white);
    box-shadow: 0 4px 10px rgba(0,0,0,0.25);
    overflow: hidden;
  }
  .wordmark {
    display: flex; align-items: center; gap: 10px;
    color: var(--brand-blue); font-weight: 700; letter-spacing: 0.5px;
    line-height: 1.1;
  }
  .wordmark .mark-square {
    width: 18px; height: 18px; background: var(--brand-blue); flex: none;
  }
  .contact { color: var(--brand-blue); font-weight: 400; line-height: 1.3; }
  .contact .name { font-weight: 700; margin-bottom: 6px; }

  /* Two-sided card, front and back laid flat */
  .card-front { left: 110px; top: 90px; width: 260px; height: 390px;
    display: flex; align-items: center; justify-content: center; }
  .card-front .wordmark { font-size: 24px; }
  .card-back { left: 470px; top: 90px; width: 260px; height: 390px;
    background: var(--brand-grey); }
  .card-back .faint-square {
    position: absolute; left: 40px; top: 40px; width: 120px; height: 120px;
    background: rgba(255,255,255,0.08);
  }
  .card-back .contact {
    position: absolute; right: 24px; bottom: 40px; text-align: right;
    color: var(--card-white); font-size: 13px;
  }

  .label {
    position: absolute;
    font-family: "Libre Baskerville", Georgia, serif;
    color: var(--brand-blue); font-size: 25px; line-height: 1.2;
  }
  .label-two-sides { right: 67px; top: 572px; color: var(--label-light); font-size: 30px; }
  .label-horizontal { right: 67px; top: 1024px; text-align: right; }
  .label-vertical { left: 390px; top: 1098px; }

  /* Single sided vertical */
  .card-vertical { left: 62px; top: 706px; width: 287px; height: 443px; text-align: center; }
  .card-vertical .wordmark { justify-content: center; font-size: 21px; margin-top: 150px; }
  .card-vertical .contact { font-size: 15px; margin-top: 44px; }
  .card-vertical .band { position: absolute; left: 0; bottom: 0; width: 100%; height: 25px; background: var(--brand-blue); }

  /* Single sided horizontal */
  .card-horizontal { left: 390px; top: 706px; width: 446px; height: 286px; }
  .card-horizontal .wordmark { position: absolute; left: 40px; top: 118px; font-size: 20px; }
  .card-horizontal .contact { position: absolute; right: 39px; top: 108px; text-align: right; font-size: 14.5px; }
  .card-horizontal .band { position: absolute; right: 0; top: 0; width: 19px; height: 100%; background: var(--brand-blue); }
</style>
</head>
<body>
  <div class="stage">
    <div class="card card-front">
      <div class="wordmark"><span class="mark-square"></span><span>CORVALE<br>IMMOBILIER</span></div>
    </div>
    <div class="card card-back">
      <div class="faint-square"></div>
      <div class="contact">
        <p class="name">Matteo ROSSANI</p>
        <p>Tél : 07 18 52 36 90</p>
        <p>rossani@felmontfrance.fr</p>
        <p>12 rue Delmas</p>
        <p>92300</p>
        <p>Levallois-Varenne</p>
      </div>
    </div>
    <p class="label label-two-sides">Two Sides</p>
  </div>

  <div class="card card-vertical">
    <div class="wordmark"><span class="mark-square"></span><span>CORVALE<br>IMMOBILIER</span></div>
    <div class="contact">
      <p class="name">Matteo ROSSANI</p>
      <p>Tél : 07 18 52 36 90</p>
      <p>rossani@felmontfrance.fr</p>
      <p>12 rue Delmas</p>
      <p>92300</p>
      <p>Levallois-Varenne</p>
    </div>
    <div class="band"></div>
  </div>

  <div class="card card-horizontal">
    <div class="wordmark"><span class="mark-square"></span><span>CORVALE<br>IMMOBILIER</span></div>
    <div class="contact">
      <p class="name">Matteo ROSSANI</p>
      <p>Tél : 07 18 52 36 90</p>
      <p>rossani@felmontfrance.fr</p>
      <p>12 rue Delmas</p>
      <p>92300</p>
      <p>Levallois-Varenne</p>
    </div>
    <div class="band"></div>
  </div>

  <p class="label label-horizontal">Single sided<br>horizontal</p>
  <p class="label label-vertical">Single sided<br>vertical</p>
</body>
</html>
```